Diseñar tarjeta de presentación/Business Card design

The Project basically consists in creating a business card for a Food Truck Company in Mexicali B.C. Mexico. The business card must contain the owner basic information with possibility to edit for another two co-founders. The BC must have design and letters in both sides and if it’s necessary images or graphics.
Content it’s mentioned below:

Front:
(ADAPTED LOGO)
TOLVANEZ FOOD TRUCK CO.
STREET&CATERING

Reverse:
Julián Pardo Ruiz
Cocinero Propietario
Cel. +52 (686) 3-82-15-94
Facebook: Tolvanez Food Truck
E-mail: chef_julianpardo@correo-ejemplo.mx

Specifications:
Preferably black and white
ILL Illustrator format and image
Free source
Just logo silhouette (unfilled)
Distance legible
No google pre-designed images, except for Facebook or e-mail logo instead of words, etc.
Minimalist and creative
Horizontal or vertical

Thank you

```html
<!DOCTYPE html>
<html lang="es">
<head>
<meta charset="utf-8">
<title>Tolvanez Food Truck Co. — Tarjeta de presentación</title>
<link rel="stylesheet" href="https://fonts.googleapis.com/css2?family=Arimo:wght@400;700&display=swap">
<style>
  :root {
    --page-bg: #e6e6e6;
    --card-bg: #ffffff;
    --ink: #4a4a4a;
    --ink-soft: #6d6d6d;
    --art-tone: #d9d9d9;
    --card-shadow: rgba(0, 0, 0, 0.18);
  }
  * { box-sizing: border-box; margin: 0; padding: 0; }
  html, body {
    width: 1200px;
    height: 800px;
    overflow: hidden;
    background: var(--page-bg);
    font-family: "Arimo", Arial, sans-serif;
    color: var(--ink);
  }
  .canvas {
    width: 1200px;
    height: 800px;
    display: flex;
    align-items: center;
    justify-content: center;
    gap: 60px;
  }
  .card {
    width: 525px;
    height: 300px;
    background: var(--card-bg);
    box-shadow: 0 10px 30px var(--card-shadow);
    position: relative;
  }

  /* Front */
  .card--front {
    display: flex;
    flex-direction: column;
    align-items: center;
    justify-content: center;
  }
  .mascot-art {
    width: 150px;
    height: 82px;
    background: linear-gradient(180deg, var(--art-tone), #c9c9c9);
    border-radius: 6px;
  }
  .brand-name {
    margin-top: 10px;
    font-weight: 700;
    font-size: 34px;
    letter-spacing: 1px;
    color: var(--ink);
  }
  .brand-sub {
    font-weight: 700;
    font-size: 10px;
    letter-spacing: 2px;
    color: var(--ink);
    margin-top: 2px;
  }
  .tagline {
    margin-top: 14px;
    font-weight: 700;
    font-size: 14px;
    letter-spacing: 0.3px;
    color: var(--ink-soft);
  }

  /* Back */
  .card--back {
    padding: 80px 0 0 70px;
  }
  .contact-list { list-style: none; }
  .contact-item {
    display: flex;
    align-items: center;
    gap: 10px;
    font-size: 15px;
    line-height: 24px;
    color: var(--ink-soft);
  }
  .contact-item svg {
    width: 12px;
    height: 12px;
    flex: none;
    fill: var(--ink);
  }
  .contact-item--name { color: var(--ink); font-weight: 700; }
</style>
</head>
<body>
<main class="canvas">
  <section class="card card--front" aria-label="Frente de la tarjeta">
    <div class="mascot-art" role="img" aria-label="Ilustración lineal de un cerdo, silueta del logotipo"></div>
    <div class="brand-name">TOLVANEZ</div>
    <div class="brand-sub">FOOD TRUCK CO.</div>
    <p class="tagline">Tolvanez Food Truck Co. Street &amp; Catering</p>
  </section>

  <section class="card card--back" aria-label="Reverso de la tarjeta">
    <ul class="contact-list">
      <li class="contact-item contact-item--name">
        <svg viewBox="0 0 12 12"><circle cx="6" cy="3.5" r="2.7"/><path d="M1 12a5 5 0 0 1 10 0z"/></svg>
        Julián Pardo Ruiz
      </li>
      <li class="contact-item">
        <svg viewBox="0 0 12 12"><rect x="2" y="5" width="8" height="6"/><rect x="3" y="1" width="6" height="3.5" rx="1.5"/></svg>
        Cocinero Propietario
      </li>
      <li class="contact-item">
        <svg viewBox="0 0 12 12"><rect x="3" y="0.5" width="6" height="11" rx="1.2"/></svg>
        Cel. +52 (686) 3-82-15-94
      </li>
      <li class="contact-item">
        <svg viewBox="0 0 12 12"><rect x="1" y="1" width="10" height="10"/></svg>
        Facebook: Tolvanez Food Truck
      </li>
      <li class="contact-item">
        <svg viewBox="0 0 12 12"><path d="M0.5 2.5h11v7h-11z"/><path d="M0.5 2.5l5.5 4 5.5-4" fill="none" stroke="#fff" stroke-width="1"/></svg>
        E-mail: chef_julianpardo@correo-ejemplo.mx
      </li>
    </ul>
  </section>
</main>
</body>
</html>
```